Business Cards for Tech Company - uBrightowl

We would like new modern business cards designed for our company. Attached are some examples of other business cards we like. <br/><br/>Info we need is: <br/>First Name, Last Name<br/>Address<br/>Store Phone<br/>Cell Phone<br/>Email Address<br/>Text Logo <br/>And Other Logo<br/>

Industry/Entity Type

Technology Equipment

Contact Information for Business Card

Please use these details as example:

Dale Morrow
Technology Specialist
Direct 555.617.2094
Phone 555-730-8186

dale.morrow@ubrightowl.example

2971 Willet Lane
Larkfield, KS 00427

Font styles to use
Sans Serif
Other font styles liked:
• Anything easy to read and modern

Colors

Designer to choose colors to be used in the design.

Requirements
Must have
• Both Logos
• Signature as name
• Use the text logo and use the shark logo but do not use the full shark logo. Have it where it is zoomed in and is expanding out of the card.
Nice to have
• Keep it clean and modern
• We like blue, white, and black/grays.
Should not have
• Random icons for phone and address.

```html
<!DOCTYPE html>
<html lang="en">
<head>
<meta charset="utf-8">
<title>uBrightowl Business Cards</title>
<link rel="stylesheet" href="https://fonts.googleapis.com/css2?family=Poppins:wght@600&family=Roboto:wght@300;400&display=swap">
<style>
  :root {
    --brand-blue: #3a72b8;
    --brand-blue-light: #2f9ad8;
    --card-white: #fbfbfb;
    --card-shade: #e6e6e6;
    --ink: #3a3a3a;
    --rule: #9a9a9a;
    --backdrop: #d9d6d2;
  }
  * { margin: 0; padding: 0; box-sizing: border-box; }
  html, body { width: 1200px; height: 900px; overflow: hidden; }
  body {
    background: var(--backdrop);
    display: flex; flex-direction: column; align-items: center; justify-content: center;
    gap: 44px;
    font-family: "Roboto", sans-serif;
  }
  .card {
    width: 600px; height: 343px; border-radius: 16px;
    position: relative; overflow: hidden;
    box-shadow: 0 10px 24px rgba(0,0,0,.22);
  }

  /* Front */
  .card-front { background: var(--brand-blue); color: #fff; }
  .brand-lockup {
    position: absolute; left: 0; right: 0; top: 108px;
    display: flex; align-items: center; justify-content: center; gap: 16px;
  }
  .brand-dot { width: 52px; height: 52px; border-radius: 50%; background: #fff; }
  .brand-text { display: flex; flex-direction: column; }
  .brand-name {
    font-family: "Poppins", sans-serif; font-weight: 600; font-size: 56px; line-height: 1;
    color: #fff; letter-spacing: -0.5px;
  }
  .brand-tagline {
    font-size: 9px; letter-spacing: 5px; text-align: right; margin-top: 4px; opacity: .85;
  }
  .front-web {
    position: absolute; left: 0; right: 0; bottom: 62px; text-align: center;
    font-size: 15px; letter-spacing: 3px; font-weight: 300;
  }

  /* Back */
  .card-back { background: linear-gradient(160deg, var(--card-white) 40%, var(--card-shade)); color: var(--ink); }
  .edge-tab { position: absolute; width: 16px; height: 92px; background: var(--brand-blue); }
  .edge-tab-left { left: 0; bottom: 36px; }
  .edge-tab-right { right: 0; top: 36px; }
  .identity {
    position: absolute; left: 60px; top: 116px; width: 250px; text-align: right; white-space: nowrap;
  }
  .person-name {
    font-family: "Poppins", sans-serif; font-weight: 600; font-size: 31px; color: var(--brand-blue); line-height: 1.1;
  }
  .person-title { font-size: 17px; margin-top: 2px; }
  .divider { position: absolute; left: 326px; top: 96px; width: 1px; height: 94px; background: var(--rule); }
  .contact-list { position: absolute; left: 342px; top: 96px; list-style: none; }
  .contact-list li { display: flex; align-items: center; gap: 8px; font-size: 14px; height: 23.5px; white-space: nowrap; }
  .icon { width: 16px; height: 16px; flex: none; }
  .address {
    position: absolute; left: 0; right: 0; bottom: 44px;
    display: flex; align-items: center; justify-content: center; gap: 6px; font-size: 14px;
  }
</style>
</head>
<body>

<section class="card card-front">
  <div class="brand-lockup">
    <div class="brand-dot"></div>
    <div class="brand-text">
      <span class="brand-name">uBrightowl</span>
      <span class="brand-tagline">TECHNOLOGIES</span>
    </div>
  </div>
  <p class="front-web">www.ubrightowl.example</p>
</section>

<section class="card card-back">
  <div class="edge-tab edge-tab-left"></div>
  <div class="edge-tab edge-tab-right"></div>

  <div class="identity">
    <h1 class="person-name">Dale Morrow</h1>
    <p class="person-title">Technology Specialist</p>
  </div>
  <div class="divider"></div>

  <ul class="contact-list">
    <li>
      <svg class="icon" viewBox="0 0 16 16"><circle cx="8" cy="8" r="8" fill="var(--brand-blue-light)"/><path d="M5.2 4.2l1.6-.3.8 2-1 .8a5 5 0 0 0 2.7 2.7l.8-1 2 .8-.3 1.6c-3.7.3-6.9-2.9-6.6-6.6z" fill="#fff"/></svg>
      555.617.2094
    </li>
    <li>
      <svg class="icon" viewBox="0 0 16 16"><circle cx="8" cy="8" r="8" fill="var(--brand-blue-light)"/><rect x="5.5" y="3.5" width="5" height="9" rx="1" fill="none" stroke="#fff" stroke-width="1.2"/></svg>
      555-730-8186
    </li>
    <li>
      <svg class="icon" viewBox="0 0 16 16"><circle cx="8" cy="8" r="8" fill="var(--brand-blue-light)"/><rect x="4" y="5" width="8" height="6" fill="none" stroke="#fff" stroke-width="1.1"/><path d="M4 5l4 3.5L12 5" fill="none" stroke="#fff" stroke-width="1.1"/></svg>
      dale.morrow@ubrightowl.example
    </li>
    <li>
      <svg class="icon" viewBox="0 0 16 16"><circle cx="8" cy="8" r="8" fill="var(--brand-blue-light)"/><g fill="none" stroke="#fff" stroke-width="1"><circle cx="8" cy="8" r="4.3"/><ellipse cx="8" cy="8" rx="1.8" ry="4.3"/><path d="M3.7 8h8.6"/></g></svg>
      www.ubrightowl.example
    </li>
  </ul>

  <p class="address">
    <svg class="icon" viewBox="0 0 16 16"><path d="M8 1.5a4.5 4.5 0 0 0-4.5 4.5c0 3.3 4.5 8.5 4.5 8.5s4.5-5.2 4.5-8.5A4.5 4.5 0 0 0 8 1.5z" fill="var(--brand-blue)"/><circle cx="8" cy="6" r="1.6" fill="#fff"/></svg>
    2971 Willet Lane, Larkfield, KS 00427
  </p>
</section>

</body>
</html>
```